Website for enterprise software start-up

We need a new Wordpress website. We are an early stage start-up focused on mobile video technology for cellular operators. The audience is strategy, marketing and customer acquisition execs from the operators.

The purpose of the site is to act as a sales brochure and capture leads. A demo app can be downloaded from the current site, want to put that behind a contact form.

Current website is at www.brevlane.tv. Similar number of pages. Looking for a clean design template, with minimal customization. Blog will remain as is.

Want to be able to modify the copy via Wordpress. Reference designs I like: tarnwick.com, tessel4analytics.com

Target Market(s)

Mobile operators and MVNOs in the US and Asia Pacific regions

Industry/Entity Type

Business Software

Coding

Coded - Design and coding required

Number of Pages Required

4 page

Font styles to use
Sans Serif

Colors
f78f20

Requirements
Must have
• Form for downloading sample apps.
• Landing page with image, Product, Blog, About, Contact
• Team page

```html
<!DOCTYPE html>
<html lang="en">
<head>
<meta charset="utf-8">
<title>Brevlane Media – High Quality Mobile Engagement</title>
<link rel="stylesheet" href="https://fonts.googleapis.com/css2?family=Fira+Sans:wght@300;400;500&family=Josefin+Slab:wght@300;400&display=swap">
<style>
  :root {
    --brand-orange: #f78f20;
    --ink-white: #ffffff;
    --ink-soft: #e9e4df;
    --ink-muted: #b9b1aa;
    --bg-deep: #120b08;
    --bg-warm: #3a2418;
    --bg-light: #e8d3bb;
    --rule: rgba(255,255,255,0.14);
  }
  * { box-sizing: border-box; margin: 0; padding: 0; }
  html, body { width: 1200px; height: 900px; overflow: hidden; background: var(--bg-deep); }
  body { font-family: "Fira Sans", Arial, sans-serif; color: var(--ink-white); position: relative; }

  .hero-photo {
    position: absolute; inset: 0;
    background:
      radial-gradient(ellipse 55% 60% at 80% 30%, rgba(246,230,210,0.95), rgba(220,180,140,0.55) 45%, rgba(0,0,0,0) 75%),
      radial-gradient(ellipse 40% 45% at 75% 65%, rgba(170,110,70,0.55), rgba(0,0,0,0) 70%),
      linear-gradient(90deg, var(--bg-deep) 0%, #1e120c 30%, var(--bg-warm) 50%, #6b4a33 70%, #a88463 100%);
  }
  .hero-shade {
    position: absolute; left: 0; right: 0; bottom: 0; height: 340px;
    background: linear-gradient(180deg, rgba(18,11,8,0) 0%, rgba(18,11,8,0.75) 55%, rgba(18,11,8,0.92) 100%);
  }

  .site-header { position: absolute; top: 27px; left: 74px; right: 60px; height: 44px; display: flex; align-items: center; justify-content: space-between; }
  .brand { display: flex; align-items: center; gap: 10px; font-family: "Fira Sans", sans-serif; font-weight: 500; font-size: 30px; color: var(--ink-white); letter-spacing: -0.3px; }
  .brand-mark { width: 42px; height: 42px; background: var(--brand-orange); }
  .main-nav { display: flex; align-items: center; gap: 37px; font-size: 15px; font-weight: 400; letter-spacing: 0.3px; }
  .main-nav a { color: var(--ink-white); text-decoration: none; }
  .main-nav .login { border: 2px solid var(--ink-white); padding: 8px 14px; margin-left: 4px; }

  .hero-copy { position: absolute; left: 73px; top: 268px; }
  .hero-title { font-family: "Josefin Slab", Georgia, serif; font-weight: 400; font-size: 40px; line-height: 42px; color: var(--ink-white); }
  .hero-title .accent { color: var(--brand-orange); }
  .hero-title sup { font-size: 9px; vertical-align: top; position: relative; top: 6px; }
  .hero-lede { margin-top: 16px; font-size: 18px; font-weight: 300; line-height: 26px; color: var(--ink-white); }

  .store-badges { position: absolute; top: 467px; left: 74px; display: flex; gap: 20px; }
  .store-badge { width: 205px; height: 64px; border-radius: 8px; background: #0a0a0a; border: 2px solid #8e8e8e; }

  .features { position: absolute; top: 680px; left: 73px; display: flex; gap: 70px; }
  .feature { width: 470px; }
  .feature h2 { font-family: "Josefin Slab", Georgia, serif; font-weight: 400; font-size: 30px; color: var(--brand-orange); line-height: 36px; }
  .feature p { margin-top: 14px; font-size: 19px; font-weight: 300; line-height: 28px; color: var(--ink-white); }
  .feature .more { display: inline-flex; align-items: center; gap: 4px; margin-top: 10px; font-size: 13px; font-weight: 500; color: var(--brand-orange); text-decoration: none; }

  .site-footer { position: absolute; left: 0; right: 0; bottom: 0; height: 47px; border-top: 1px solid var(--rule); display: flex; align-items: center; justify-content: center; font-size: 13px; color: var(--ink-muted); }
</style>
</head>
<body>
  <div class="hero-photo" role="img" aria-label="Photograph of a woman holding a smartphone that plays a music video"></div>
  <div class="hero-shade"></div>

  <header class="site-header">
    <div class="brand"><span class="brand-mark"></span>Brevlane Media</div>
    <nav class="main-nav">
      <a href="#">HOME</a>
      <a href="#">PRODUCT</a>
      <a href="#">BLOG</a>
      <a href="#">ABOUT</a>
      <a href="#">CONTACT</a>
      <a href="#" class="login">LOGIN</a>
    </nav>
  </header>

  <section class="hero-copy">
    <h1 class="hero-title">High Quality<br><span class="accent">Mobile Engagement<sup>TM</sup></span></h1>
    <p class="hero-lede">We engage mobile audiences with the right<br>video content at the perfect moment.</p>
  </section>

  <div class="store-badges">
    <span class="store-badge" aria-label="App store download"></span>
    <span class="store-badge" aria-label="App store download"></span>
  </div>

  <section class="features">
    <article class="feature">
      <h2>Push Video Notifications</h2>
      <p>Personalised flawless HD videos, revealed at the perfect moment, as rich media notifications.</p>
      <a href="#" class="more">Learn More</a>
    </article>
    <article class="feature">
      <h2>Native Push Video</h2>
      <p>Personalised flawless HD videos, discoverable in-app, and playable even when offline.</p>
      <a href="#" class="more">Learn More
        <svg width="11" height="10" viewBox="0 0 11 10" aria-hidden="true"><path d="M1 5h8M5.5 1.5L9 5l-3.5 3.5" stroke="#f78f20" stroke-width="2" fill="none"/></svg>
      </a>
    </article>
  </section>

  <footer class="site-footer">© 2016 Brevlane Media, Inc. Privacy Policy</footer>
</body>
</html>
```